Lantern Dynamics Web Design Project

We need to update our web design for our company. Lantern Dynamics™ is a series of Development (Training) Programs that we deliver both for the General Public as well as Corporate Business.

Much of the content needs a refresh but we are keen to get some thoughts now on design and layout, predominantly front page. Happy to take any comments on the content if you think that is relevant as well.

We might look to move the current video clip and bring a more generic 'inspirational' clip to the front page. A good example of this is www.mindcrestlearn.com.au

Our courses have a very similar market to Gregory Halvern type courses ... both General Public and Corporate business.

Refer our website www.lanterndynamics.com

Target Market(s)

General Public as well as Corporate Business. Courses are designed for all. Gregory Halvern would be a good 'feel' for what we do.

Industry/Entity Type

Business

Requirements
Must have
• Must have a 'leading edge' type feel to it.
Must look professional.

```html
<!DOCTYPE html>
<html lang="en">
<head>
<meta charset="utf-8">
<title>Lantern Dynamics</title>
<link href="https://fonts.googleapis.com/css2?family=Roboto+Condensed:wght@400;700&family=Roboto:ital,wght@0,400;1,400&display=swap" rel="stylesheet">
<style>
:root{
  --blue:#1a75c4;
  --nav:#2a8fe0;
  --link:#1a72c0;
  --grey-bg:#efefef;
  --text:#555;
  --heading:#555;
  --btn:#6a6a6a;
  --footer:#333;
  --footer-deep:#222;
  --white:#fff;
}
*{margin:0;padding:0;box-sizing:border-box}
html,body{width:992px;height:1200px;overflow:hidden}
body{position:relative;font-family:"Roboto",Arial,sans-serif;color:var(--text);background:var(--grey-bg)}
.abs{position:absolute}

.site-header{position:absolute;left:0;top:0;width:992px;height:120px;background:var(--blue)}
.brand{position:absolute;left:99px;top:36px;display:flex;align-items:center;gap:10px;color:var(--white);font-family:"Roboto Condensed",sans-serif;font-size:30px;line-height:1}
.brand-dot{width:14px;height:14px;border-radius:50%;background:var(--white)}
.search{position:absolute;left:684px;top:47px;width:208px;height:30px;background:var(--white);border:2px solid #d6e4f1;border-radius:3px}
.search svg{position:absolute;right:8px;top:7px}

.main-nav{position:absolute;left:0;top:120px;width:992px;height:37px;background:linear-gradient(#3a9ae6,var(--nav));border-top:1px solid #57aaeb}
.main-nav ul{list-style:none;display:flex;position:absolute;left:111px;top:11px;font-family:"Roboto Condensed",sans-serif;font-size:12.5px;color:var(--white);text-transform:uppercase}
.main-nav li{margin-right:29px}

.hero{position:absolute;left:0;top:157px;width:992px;height:300px;background:var(--blue)}
.hero-video{position:absolute;left:107px;top:30px;width:397px;height:231px;background:linear-gradient(160deg,#6f7a6a,#a89a86 40%,#c45a3e 80%,#d9543a)}
.play{position:absolute;left:172px;top:84px;width:70px;height:70px;background:rgba(80,80,80,.45);border-radius:4px}
.play svg{position:absolute;left:24px;top:20px}
.hero-copy{position:absolute;left:525px;top:36px;color:var(--white);font-family:"Roboto Condensed",sans-serif;text-transform:uppercase}
.hero-copy .kicker{font-size:20px;line-height:24px}
.hero-copy .tagline{font-size:27.5px;line-height:35px;margin-top:20px;letter-spacing:.5px}
.hero-copy .lead{font-size:19.5px;line-height:24px;margin-top:13px}
.slider-dots{position:absolute;left:463px;top:278px;display:flex;gap:13px}
.slider-dots span{width:12px;height:12px;border-radius:50%;background:#5d7d9a;border:2px solid #b9c9d8}
.slider-dots span:first-child{background:#ddd}

.card{position:absolute;top:469px;width:190px;height:230px;background:var(--white);box-shadow:0 0 2px rgba(0,0,0,.15);padding:6px 5px}
.card h3{font-family:"Roboto Condensed",sans-serif;font-weight:400;font-size:12.5px;line-height:17px;text-transform:uppercase;color:var(--link)}
.card h3 span{display:block;color:var(--heading);font-size:14px}
.card .thumb{height:83px;margin-top:12px}
.card p{font-size:9.5px;line-height:12px;margin-top:9px;text-align:justify;height:48px}
.btn-more{display:inline-block;margin-top:6px;background:var(--btn);color:var(--white);font-family:"Roboto Condensed",sans-serif;font-size:10px;padding:6px 6px;text-transform:uppercase}

.section-title{font-family:"Roboto Condensed",sans-serif;font-weight:400;font-size:14.5px;line-height:18px;text-transform:uppercase;color:var(--heading);padding-bottom:11px;border-bottom:1px solid #d4d4d4}
.section-title em{font-style:normal;color:var(--link)}
.welcome{left:99px;top:733px;width:249px}
.welcome p{font-size:9px;line-height:13.2px;margin-top:11px}
.welcome ul{list-style:none;margin-top:17px;font-size:9px;line-height:11.5px}
.welcome li{position:relative;padding-left:12px;margin-bottom:4px}
.welcome li::before{content:"";position:absolute;left:0;top:2px;border-left:5px solid var(--link);border-top:4px solid transparent;border-bottom:4px solid transparent}
.events{left:372px;top:733px;width:248px}
.event{border-bottom:1px solid #d4d4d4;padding:11px 0 7px;font-size:9px;line-height:14.5px}
.event:last-child{border-bottom:0;padding-bottom:0}
.event h4{font-weight:400;color:var(--link);font-size:10px;line-height:12px;margin-bottom:6px}
.event a{color:var(--link);text-decoration:none}

.newsletter{position:absolute;left:645px;top:730px;width:248px;height:227px;background:var(--blue)}
.newsletter h2{font-family:"Roboto Condensed",sans-serif;font-weight:400;font-size:15.5px;color:var(--white);padding:13px 9px 12px;border-bottom:1px solid #3e8ed4;text-transform:uppercase}
.field{position:absolute;left:9px;width:231px;height:29px;background:var(--white);border:1px solid #cfdbe6;border-radius:2px;font-size:8.5px;color:#666;padding:9px 9px}
.btn-signup{position:absolute;left:165px;top:185px;width:75px;height:29px;background:linear-gradient(#2e92e6,#1c7bd0);border:1px solid #5aa9ea;border-radius:3px;color:var(--white);font-family:"Roboto Condensed",sans-serif;font-size:14px;text-align:center;line-height:27px}

.site-footer{position:absolute;left:0;top:958px;width:992px;height:183px;background:var(--footer)}
.fcol{position:absolute;top:42px;font-size:9.5px;color:#ddd}
.fcol h5{position:absolute;top:-42px;left:0;width:200px;font-family:"Roboto Condensed",sans-serif;font-weight:400;font-size:11.5px;color:var(--white);text-transform:uppercase;padding:10px 7px 8px;border-bottom:1px solid #555}
.fcol ul{list-style:none;line-height:16.5px}
.fcol address{font-style:normal;line-height:14px}
.quote{font-style:italic;font-size:10px;line-height:15px;color:#ddd}
.qmark{font-family:Georgia,serif;font-size:28px;color:#666;line-height:1}
.bottom-bar{position:absolute;left:0;top:1141px;width:992px;height:59px;background:var(--footer-deep)}
.copyright{position:absolute;left:96px;top:24px;font-size:9.5px;color:var(--white)}
.social{position:absolute;left:732px;top:17px;display:flex;gap:7px}
.social span{width:26px;height:26px;display:block}
</style>
</head>
<body>

<header class="site-header">
  <div class="brand"><span class="brand-dot"></span>Lantern Dynamics™</div>
  <div class="search">
    <svg width="12" height="12" viewBox="0 0 12 12"><circle cx="5" cy="5" r="3.5" fill="none" stroke="#bbb" stroke-width="1.3"/><line x1="7.5" y1="7.5" x2="11" y2="11" stroke="#bbb" stroke-width="1.6"/></svg>
  </div>
</header>

<nav class="main-nav">
  <ul>
    <li>Home</li><li>Lantern Dynamics™</li><li>About Us</li><li>Our Programs</li><li>Events</li><li>Our Products</li><li>Articles &amp; Resources</li><li>Contact Us</li>
  </ul>
</nav>

<section class="hero">
  <div class="hero-video" role="img" aria-label="Video still of a presenter outdoors in front of a stone building">
    <div class="play"><svg width="24" height="30" viewBox="0 0 24 30"><polygon points="0,0 24,15 0,30" fill="rgba(200,200,200,.6)"/></svg></div>
  </div>
  <div class="hero-copy">
    <div class="kicker">Discover Lantern Dynamics™ -<br>Watch our clip!</div>
    <div class="tagline">A new way of thinking to<br>create a new way of being.</div>
    <div class="lead">Lantern Dynamics delivers leading edge<br>workshops, seminars and products in a<br>fun and interactive way.</div>
  </div>
  <div class="slider-dots"><span></span><span></span><span></span></div>
</section>

<article class="card" style="left:99px">
  <h3>Lantern Dynamics™<span>For You</span></h3>
  <div class="thumb" role="img" aria-label="Person with arms raised on a green field under blue sky" style="background:linear-gradient(#9cc3e6,#dbe9f4 70%,#7cbf3a 82%,#5a9a2a)"></div>
  <p>Experience the latest leading edge programs that will totally change how you view yourself and the world you operate within....</p>
  <span class="btn-more">More Info</span>
</article>
<article class="card" style="left:300px">
  <h3>Lantern Dynamics™<span>For Children and Schools</span></h3>
  <div class="thumb" role="img" aria-label="Smiling school children in a classroom" style="background:linear-gradient(90deg,#c97a4a,#e3a57a 40%,#5a8fc8 60%,#d98a55)"></div>
  <p>Our programs are specifically designed for children and also to support School educational programs. They focus on Lantern Dynamics™ ..</p>
  <span class="btn-more">More Info</span>
</article>
<article class="card" style="left:501px">
  <h3>Lantern Dynamics™<span>For Business</span></h3>
  <div class="thumb" role="img" aria-label="Hands holding a glowing world map" style="background:radial-gradient(circle at 50% 40%,#cfe9fb,#3a8fd0 55%,#0d4f96)"></div>
  <p>We work alongside our clients to understand your areas of focus and then design a program that supports you and your business to achieve this...</p>
  <span class="btn-more">More Info</span>
</article>
<article class="card" style="left:703px">
  <h3>Lantern Dynamics™<span>For Community</span></h3>
  <div class="thumb" role="img" aria-label="Hands joined into a peace sign against the sky" style="background:linear-gradient(120deg,#bfe0f5,#e8c3a8 50%,#b86a40 75%,#dcebf5)"></div>
  <p>Experience the latest leading edge programs that will totally change how you view yourself and the world you operate within....</p>
  <span class="btn-more">More Info</span>
</article>

<section class="abs welcome">
  <h2 class="section-title">Welcome to <em>Lantern Dynamics™</em></h2>
  <p>Lantern Dynamics™ is a leading edge model which introduces a new lens to view yourself and the world you operate within. Lantern Dynamics™ is for everyone. It's all about Transformation and Skills for Life.</p>
  <ul>
    <li>Improve your health and wellbeing</li>
    <li>Create a new fun and healthy culture</li>
    <li>Learn new ways to manage stress and create balance<br>in your life</li>
    <li>Enhance your communication skills and strengthen<br>your relationships</li>
    <li>Learn new ways to Transform and create all that you<br>have ever wanted</li>
  </ul>
</section>

<section class="abs events">
  <h2 class="section-title">Upcoming Events</h2>
  <div class="event"><h4>JUNE 2013</h4>Health &amp; Wellbeing - Sat 16 Jun - Melbourne, Australia -<br><a>Register Now</a></div>
  <div class="event"><h4>JUNE 2013</h4>Health &amp; Wellbeing - Sat 16 Jun - Melbourne, Australia -<br><a>Register Now</a></div>
  <div class="event"><h4>JUNE 2013</h4>Health &amp; Wellbeing - Sat 16 Jun - Melbourne, Australia -<br><a>Register Now</a></div>
</section>

<section class="newsletter">
  <h2>Sign up to our newsletter</h2>
  <div class="field" style="top:58px">First name:</div>
  <div class="field" style="top:101px">Surname:</div>
  <div class="field" style="top:144px">Email:</div>
  <div class="btn-signup">SIGN UP</div>
</section>

<footer class="site-footer">
  <div class="fcol" style="left:99px">
    <h5>Testimonials</h5>
    <div class="qmark" style="margin-top:-6px">&ldquo;</div>
    <p class="quote" style="margin:-14px 0 0 17px;width:170px">We can't solve problems by using the same kind of thinking we used when we created them</p>
    <p style="margin:10px 0 0 16px;font-size:10px">– MARCUS ELLWOOD</p>
    <div class="qmark" style="margin:-6px 0 0 173px">&rdquo;</div>
  </div>
  <div class="fcol" style="left:306px">
    <h5>Our Programmers</h5>
    <ul><li>For You</li><li>For Children and Schools</li><li>For Business</li><li>For Animals</li><li>For Community</li><li>For Practitioner</li></ul>
  </div>
  <div class="fcol" style="left:508px">
    <h5>Informations</h5>
    <ul><li>Lantern Dynamics™</li><li>About Us</li><li>Our Programs</li><li>Events</li><li>Our Products</li><li>Articles &amp; Resources</li></ul>
  </div>
  <div class="fcol" style="left:705px">
    <h5>Contact Info</h5>
    <address>PO Box 418<br>Harbour Lane East<br>Vic 8120 Australia<br><br>Phone: +61 (3) 9555 0148<br>Mob: +61 (0) 400 555 271<br>Email: info@lanterndynamics.com</address>
  </div>
</footer>

<div class="bottom-bar">
  <div class="copyright">Copyright © 2013 Lantern Dynamics</div>
  <div class="social">
    <span style="background:#3b5a9a" aria-label="Social link"></span>
    <span style="background:#1aa3e0" aria-label="Social link"></span>
    <span style="background:#c8232c" aria-label="Social link"></span>
    <span style="background:#c4171b" aria-label="Social link"></span>
    <span style="background:#d6402e" aria-label="Social link"></span>
  </div>
</div>

</body>
</html>
```